Specialized Personal Trainer Needs a Business Card Design

I need a business card design for my personal training business called Tall Oak Fitness. I have my Human Kinetics degree in Exercise Science from the Halvern Ridge University as well as an extra certification from NBEP (National Board of Exercise Practice). I work as a Cardiac Rehab Exercise Specialist and personal trainer giving specialized exercise prescriptions to those that have different heart conditions as well as work with the general population in weight loss, strength and conditioning, getting/staying fit.
Updates

I decided that I wanted a logo (as I did not have one before I submitted my project for a business card) so I am submitting a project to get a logo done and then I will decide on a business card, hopefully being able to use one of the designs already submitted.  My apologies for doing this backwards.  I am new to this so I appreciate your patience.

Thank you.

Hi, I have just created a project for a logo design (I realized I needed a logo and I should've done that first..oops!), please feel free to participate.  Once I receive a logo I like I will finalize my business card project and hopefully incorporate it into one of your business card designs. 

Thank you!

Target Market(s)

Business professionals

Industry/Entity Type

Personal Trainer

Requirements
Must have
• My name with my info:
Celia R. Dunhill (BHK)
NBEP Certified Clinical Exercise Specialist & Personal Trainer
celia.dunhill@talloakfitness.example
Cell: 604-358-4170

Please make it double sided.
Nice to have
• An image that represents cardiac and general fitness training.

```html
<!DOCTYPE html>
<html lang="en">
<head>
<meta charset="utf-8">
<title>Tall Oak Fitness – Business Card</title>
<link rel="stylesheet" href="https://fonts.googleapis.com/css2?family=Signika:wght@700&family=Bitter:wght@700;900&display=swap">
<style>
  :root {
    --stage: #ececec;
    --logo-teal: #1d6b6e;
    --contact-blue: #1a2fc9;
    --info-red: #b3120f;
    --rule-red: #7a0d0d;
    --sky-top: #3c8fe0;
    --sky-low: #e9f6fb;
    --grass-top: #6fd14a;
    --grass-low: #1f9a2c;
    --photo-red: #c9242b;
    --photo-blue: #2aa6d8;
    --figure-blue: #2f6fd0;
    --icon-blue: #2747c7;
    --icon-green: #2e9e3a;
  }
  * { box-sizing: border-box; margin: 0; padding: 0; }
  html, body { width: 1200px; height: 900px; overflow: hidden; }
  body { background: var(--stage); position: relative; }

  .card {
    position: absolute;
    width: 560px;
    height: 320px;
    overflow: hidden;
    box-shadow: 0 8px 24px rgba(0,0,0,.25);
  }

  /* Front */
  .card-front {
    left: 80px; top: 70px;
    background: linear-gradient(120deg, #f5f1e8 0%, #e94a2c 45%, #f3c623 70%, #2b8fd1 100%);
  }
  .brand {
    position: absolute;
    left: 26px; top: 38px;
    font-family: "Signika", "Verdana", sans-serif;
    font-weight: 700;
    color: var(--logo-teal);
    line-height: 1.02;
    font-size: 72px;
    letter-spacing: -1px;
  }
  .brand span { display: block; }
  .trainer-photo {
    position: absolute;
    right: 0; top: 0;
    width: 225px; height: 100%;
    background: linear-gradient(160deg, var(--photo-red) 0%, #d64a3a 40%, var(--photo-blue) 75%, #1c1c1c 100%);
  }

  /* Back */
  .card-back {
    left: 560px; top: 480px;
    background: linear-gradient(180deg, var(--sky-top) 0%, var(--sky-low) 45%, #ffffff 55%, var(--grass-top) 62%, var(--grass-low) 100%);
  }
  .figure-art {
    position: absolute;
    right: 10px; top: 10px;
    width: 170px; height: 300px;
    border-radius: 40% 40% 10% 10%;
    background: radial-gradient(ellipse at 50% 40%, var(--figure-blue) 0%, rgba(47,111,208,.55) 45%, rgba(47,111,208,0) 72%);
  }
  .contact-heading {
    position: absolute;
    left: 16px; top: 14px;
    font-family: "Bitter", "Georgia", serif;
    font-weight: 900;
    font-size: 38px;
    color: var(--contact-blue);
    text-decoration: underline;
    text-decoration-thickness: 3px;
  }
  .info {
    position: absolute;
    left: 18px;
    font-family: "Bitter", "Georgia", serif;
    font-weight: 700;
    color: var(--info-red);
    font-size: 15px;
    line-height: 1.25;
  }
  .info-name { top: 84px; }
  .info-title { top: 116px; width: 380px; }
  .info-rule {
    position: absolute;
    left: 18px; top: 162px;
    width: 360px; height: 3px;
    background: var(--rule-red);
  }
  .contact-line {
    position: absolute;
    left: 18px;
    display: flex;
    align-items: center;
    gap: 8px;
    font-family: "Bitter", "Georgia", serif;
    font-weight: 700;
    font-size: 14px;
    color: var(--info-red);
  }
  .contact-email { top: 190px; }
  .contact-phone { top: 240px; }
  .contact-line svg { flex: none; }
</style>
</head>
<body>

  <section class="card card-front" aria-label="Business card front">
    <h1 class="brand"><span>Tall</span><span>Oak</span><span>Fitness</span></h1>
    <div class="trainer-photo" role="img" aria-label="Photo of a smiling trainer in a blue top holding dumbbells"></div>
  </section>

  <section class="card card-back" aria-label="Business card back">
    <div class="figure-art" role="img" aria-label="Illustration of a blue anatomical human figure with outstretched arms"></div>
    <h2 class="contact-heading">Contact me:</h2>
    <p class="info info-name">Name : Celia R. Dunhill (BHK)</p>
    <p class="info info-title">NBEP Certified Clinical Exercise Specialist &amp; Personal Trainer</p>
    <div class="info-rule"></div>
    <p class="contact-line contact-email">
      <svg width="34" height="34" viewBox="0 0 34 34" aria-hidden="true">
        <circle cx="17" cy="17" r="16" fill="var(--icon-blue)"/>
        <rect x="8" y="11" width="18" height="12" fill="#fff"/>
        <polyline points="8,11 17,18 26,11" fill="none" stroke="var(--icon-blue)" stroke-width="1.6"/>
      </svg>
      : celia.dunhill@talloakfitness.example
    </p>
    <p class="contact-line contact-phone">
      <svg width="34" height="34" viewBox="0 0 34 34" aria-hidden="true">
        <rect x="1" y="1" width="32" height="32" rx="5" fill="var(--icon-green)"/>
        <path d="M11 9 L15 9 L16 14 L13.5 15.5 Q15.5 20 18.5 21 L20 18.5 L25 19.5 L25 23.5 Q24 25 22 25 Q10 23 9 11 Q9 9 11 9 Z" fill="#fff"/>
      </svg>
      : 604-358-4170
    </p>
  </section>

</body>
</html>
```